Voterra Reserve new label design.

Voterra needs a new image that communicates quality, authenticity and modernity.
Our marketing strategy is based on competitive price and good quality.

We need the design shown below (8 wines):

1. Spanish red wine
2. Spanish red wine
3. French red wine .
4. Chilean red wine .
5. Argentine red wine .
6. Mexican red wine .
7. French red wine.
8. Italian red wine .

One base design with 8 variations and colors ... we what the Cafloria line of wine per say. Or another good example is the Brisca Fizz line.
Updates

Justo to clarify an important issue: we need a new LABEL not a new logo. You can find the logo file (voterra logo 2013-grid) on the proyect. Thanks!

Target Market(s)

Premium shoppers from wine want quality and design.

Industry/Entity Type

Marketing

Requirements
Must have
• The new logo *Find it on the files. *
Year of production.
Type of grape.
Country.
Region.
Bottles preferably with the traditional silhouette of 750 ml.
Label size it´s up to you.
Nice to have
• I uploaded some examples of "line products" , this is what we are looking for to have in Voterra Reserve.

```html
<!DOCTYPE html>
<html lang="en">
<head>
<meta charset="utf-8">
<title>Voterra Reserve – Grenache Label Line</title>
<link href="https://fonts.googleapis.com/css2?family=Alegreya:wght@400&family=Great+Vibes&display=swap" rel="stylesheet">
<style>
  :root {
    --backdrop: #1d2a17;
    --white: #ffffff;
    --ink: #1a1a1a;
    --red: #c0232b;
    --green: #74bf44;
    --orange: #e98f29;
    --teal: #63c5c4;
    --blue: #2f8cc1;
    --grey: #b5b3b1;
    --plum: #6b244f;
    --gold: #e8a82b;
  }
  * { margin: 0; padding: 0; box-sizing: border-box; }
  html, body { width: 1200px; height: 656px; overflow: hidden; }
  body { background: var(--backdrop); position: relative; }

  .label-line {
    position: absolute; left: 20px; top: 12px;
    display: grid;
    grid-template-columns: repeat(4, 285px);
    grid-template-rows: repeat(2, 305px);
    column-gap: 4px; row-gap: 20px;
  }
  .label {
    position: relative;
    background: var(--label-bg);
    color: var(--white);
    overflow: hidden;
  }
  .label--red { --label-bg: var(--red); }
  .label--green { --label-bg: var(--green); }
  .label--orange { --label-bg: var(--orange); }
  .label--teal { --label-bg: var(--teal); }
  .label--blue { --label-bg: var(--blue); }
  .label--grey { --label-bg: var(--grey); }
  .label--plum { --label-bg: var(--plum); }
  .label--gold { --label-bg: var(--gold); }

  .grape-variety {
    position: absolute; top: 12px; left: 0; right: 0;
    text-align: center;
    font-family: "Alegreya", serif; font-size: 15px; font-weight: 400;
  }
  .warrior-art {
    position: absolute; left: 92px; top: 44px; width: 116px; height: 122px;
    background: radial-gradient(ellipse at center, rgba(20,20,20,.5) 0%, rgba(20,20,20,.22) 45%, rgba(255,255,255,0) 72%);
  }
  .brand-band {
    position: absolute; left: 32px; right: 0; top: 158px; height: 42px;
    background: var(--white);
    display: flex; align-items: center; justify-content: center;
    color: var(--ink);
    font-family: "Alegreya", serif; font-weight: 400; font-size: 25px;
    white-space: nowrap;
  }

  .origin-row {
    position: absolute; top: 224px; left: 0; right: 0;
    display: flex; align-items: center; justify-content: center; gap: 6px;
  }
  .grape-cluster {
    width: 20px; height: 12px;
    background: linear-gradient(90deg, #3a3550, #5f6e3a);
    border-radius: 40%;
  }
  .wine-style { font-family: "Great Vibes", cursive; font-size: 10px; min-width: 62px; text-align: center; }
  .divider {
    position: absolute; top: 247px; left: 106px; width: 90px; height: 1px;
    background: var(--white); opacity: .85;
  }
  .region {
    position: absolute; top: 253px; left: 0; right: 0;
    text-align: center;
    font-family: "Alegreya", serif; font-size: 7px; letter-spacing: 3px;
  }
  .footer {
    position: absolute; left: 14px; right: 14px; bottom: 10px;
    display: flex; justify-content: space-between; align-items: baseline;
    font-family: "Alegreya", serif;
  }
  .footer .country-year { font-size: 10px; }
  .footer .country-year .sep { margin: 0 7px; }
  .footer .volume { font-size: 7px; }
</style>
</head>
<body>
<main class="label-line">

  <article class="label label--red">
    <p class="grape-variety">Grenache</p>
    <div class="warrior-art" role="img" aria-label="Brand illustration of an ancient warrior with shield and spear"></div>
    <h2 class="brand-band">Voterra Reserve</h2>
    <div class="origin-row"><span class="grape-cluster" role="img" aria-label="Grape cluster ornament"></span><span class="wine-style">Spanish Red Wine</span><span class="grape-cluster" role="img" aria-label="Grape cluster ornament"></span></div>
    <div class="divider"></div>
    <p class="region">RIOJA</p>
    <footer class="footer"><span class="country-year">Spain<span class="sep">|</span>2013</span><span class="volume">750 ml</span></footer>
  </article>

  <article class="label label--green">
    <p class="grape-variety">Grenache</p>
    <div class="warrior-art" role="img" aria-label="Brand illustration of an ancient warrior with shield and spear"></div>
    <h2 class="brand-band">Voterra Reserve</h2>
    <div class="origin-row"><span class="grape-cluster" role="img" aria-label="Grape cluster ornament"></span><span class="wine-style">French Red Wine</span><span class="grape-cluster" role="img" aria-label="Grape cluster ornament"></span></div>
    <div class="divider"></div>
    <p class="region">RIOJA</p>
    <footer class="footer"><span class="country-year">Spain<span class="sep">|</span>2013</span><span class="volume">750 ml</span></footer>
  </article>

  <article class="label label--orange">
    <p class="grape-variety">Grenache</p>
    <div class="warrior-art" role="img" aria-label="Brand illustration of an ancient warrior with shield and spear"></div>
    <h2 class="brand-band">Voterra Reserve</h2>
    <div class="origin-row"><span class="grape-cluster" role="img" aria-label="Grape cluster ornament"></span><span class="wine-style">Chilean Red Wine</span><span class="grape-cluster" role="img" aria-label="Grape cluster ornament"></span></div>
    <div class="divider"></div>
    <p class="region">RIOJA</p>
    <footer class="footer"><span class="country-year">Spain<span class="sep">|</span>2013</span><span class="volume">750 ml</span></footer>
  </article>

  <article class="label label--teal">
    <p class="grape-variety">Grenache</p>
    <div class="warrior-art" role="img" aria-label="Brand illustration of an ancient warrior with shield and spear"></div>
    <h2 class="brand-band">Voterra Reserve</h2>
    <div class="origin-row"><span class="grape-cluster" role="img" aria-label="Grape cluster ornament"></span><span class="wine-style">Argentine Red Wine</span><span class="grape-cluster" role="img" aria-label="Grape cluster ornament"></span></div>
    <div class="divider"></div>
    <p class="region">RIOJA</p>
    <footer class="footer"><span class="country-year">Spain<span class="sep">|</span>2013</span><span class="volume">750 ml</span></footer>
  </article>

  <article class="label label--blue">
    <p class="grape-variety">Grenache</p>
    <div class="warrior-art" role="img" aria-label="Brand illustration of an ancient warrior with shield and spear"></div>
    <h2 class="brand-band">Voterra Reserve</h2>
    <div class="origin-row"><span class="grape-cluster" role="img" aria-label="Grape cluster ornament"></span><span class="wine-style">Mexican Red Wine</span><span class="grape-cluster" role="img" aria-label="Grape cluster ornament"></span></div>
    <div class="divider"></div>
    <p class="region">RIOJA</p>
    <footer class="footer"><span class="country-year">Spain<span class="sep">|</span>2013</span><span class="volume">750 ml</span></footer>
  </article>

  <article class="label label--grey">
    <p class="grape-variety">Grenache</p>
    <div class="warrior-art" role="img" aria-label="Brand illustration of an ancient warrior with shield and spear"></div>
    <h2 class="brand-band">Voterra Reserve</h2>
    <div class="origin-row"><span class="grape-cluster" role="img" aria-label="Grape cluster ornament"></span><span class="wine-style">Italian Red Wine</span><span class="grape-cluster" role="img" aria-label="Grape cluster ornament"></span></div>
    <div class="divider"></div>
    <p class="region">RIOJA</p>
    <footer class="footer"><span class="country-year">Spain<span class="sep">|</span>2013</span><span class="volume">750 ml</span></footer>
  </article>

  <article class="label label--plum">
    <p class="grape-variety">Grenache</p>
    <div class="warrior-art" role="img" aria-label="Brand illustration of an ancient warrior with shield and spear"></div>
    <h2 class="brand-band">Voterra Reserve</h2>
    <div class="origin-row"><span class="grape-cluster" role="img" aria-label="Grape cluster ornament"></span><span class="wine-style">Spanish Red Wine</span><span class="grape-cluster" role="img" aria-label="Grape cluster ornament"></span></div>
    <div class="divider"></div>
    <p class="region">RIOJA</p>
    <footer class="footer"><span class="country-year">Spain<span class="sep">|</span>2013</span><span class="volume">750 ml</span></footer>
  </article>

  <article class="label label--gold">
    <p class="grape-variety">Grenache</p>
    <div class="warrior-art" role="img" aria-label="Brand illustration of an ancient warrior with shield and spear"></div>
    <h2 class="brand-band">Voterra Reserve</h2>
    <div class="origin-row"><span class="grape-cluster" role="img" aria-label="Grape cluster ornament"></span><span class="wine-style">French Red Wine</span><span class="grape-cluster" role="img" aria-label="Grape cluster ornament"></span></div>
    <div class="divider"></div>
    <p class="region">RIOJA</p>
    <footer class="footer"><span class="country-year">Spain<span class="sep">|</span>2013</span><span class="volume">750 ml</span></footer>
  </article>

</main>
</body>
</html>
```